Design a colorful and bold graphic for the side of my boat

Looking for bold and/or colorful options.
Must include boat name - Keep calm cast on
Boat belongs to me and my daughter - funny, fun loving and enjoy outdoors. We use it for fishing in Texas.
We are close to the same height (she is a teenager). Like something funny/punchy/sassy. Do not want anything sexy.
Would like to end up doing a vinyl print of it to adhere to both sides of boat. Needs to be narrow and long. I will remove the wording currently on the side of the boat that says gullmark boats.

The new graphic kind of sits at two different levels. The top level and then the boat notches in about an inch down to the next one.

Hello designers! Thank you for considering my project. Im looking for a fun energy design to go on the side of my boat and feature the boat name and fish.
Name - Keep Calm Cast On. Used by - my daughter and I - both females and close to the same height. I do not want the image to be sexy in any way. Would love it to show a great image of a fish or us both catching fish. We wear ballcaps with ponytails. The image does not have to contain us but certainly can. Must have fish and boat name though. I like colorful and bold designs. No not care for childish images. I do like edgy, bold, funny, eye catching. etc. My daughter and I are both funny and fun loving and love the water and fishing. Would love to have a cool graphic that captures that spirit.
This bio is hopefully helpful. I got a number of designs previously and they did not match my requests. Thank you for your creative input and considering my project.

Colors

Designer to choose colors to be used in the design.

Requirements
Must have
• Be approx 1 foot tall and 5 feet long, show boat name, and some sort of fun image of fish/s
Nice to have
• Us represented some way - mom and daughter depicted to look like fish or both of us catching fish
Should not have
• Only words

```html
<!DOCTYPE html>
<html lang="en">
<head>
<meta charset="utf-8">
<title>Keep Calm Cast On – Boat Side Graphic</title>
<link rel="stylesheet" href="https://fonts.googleapis.com/css2?family=Bebas+Neue&display=swap">
<style>
  :root {
    --backdrop: #c0c0c0;
    --banner-red: #9f1425;
    --scene-tint: #d98a93;
    --scene-tint-soft: #c4505d;
    --ink-white: #ffffff;
  }
  html, body {
    margin: 0;
    padding: 0;
    width: 1200px;
    height: 463px;
    overflow: hidden;
    background: var(--backdrop);
  }
  .canvas {
    position: relative;
    width: 1200px;
    height: 463px;
  }
  .boat-banner {
    position: absolute;
    left: 97px;
    top: 131px;
    width: 1005px;
    height: 201px;
    background: var(--banner-red);
    overflow: hidden;
  }
  .anglers-scene {
    position: absolute;
    left: 30px;
    top: 6px;
    width: 360px;
    height: 195px;
    border-radius: 6px 6px 0 0;
    background: linear-gradient(110deg, var(--scene-tint) 0%, var(--scene-tint-soft) 55%, var(--banner-red) 100%);
  }
  .dock {
    position: absolute;
    left: 0;
    top: 186px;
    width: 119px;
    height: 15px;
    background: var(--ink-white);
  }
  .boat-name {
    position: absolute;
    left: 0;
    top: 0;
    width: 1005px;
    height: 201px;
  }
  .boat-name text {
    font-family: "Bebas Neue", "Arial Narrow", sans-serif;
    font-size: 97px;
    fill: var(--ink-white);
    stroke: var(--ink-white);
    stroke-width: 2.5px;
    stroke-linejoin: miter;
  }
</style>
</head>
<body>
  <main class="canvas">
    <section class="boat-banner">
      <div class="anglers-scene" role="img" aria-label="White silhouettes of a mother and daughter in ballcaps and ponytails fishing side by side, with a school of fish swimming toward their lines"></div>
      <div class="dock"></div>
      <svg class="boat-name" viewBox="0 0 1005 201" width="1005" height="201">
        <text x="332" y="130" textLength="641" lengthAdjust="spacingAndGlyphs">KEEP CALM CAST ON</text>
      </svg>
    </section>
  </main>
</body>
</html>
```